Emergency Vehicle Installer and Security Firm Needs a Business Card

Our company "Corvalt" need a business card for our Emergency Vehicle Equipment Installation and Infrastructure Security Business. We are contract designers, manufacturers and installers for Emergency Vehicle Fleets. This includes installation of Emergency Lights, Sirens, Vehicle Graphics and Radio Communications. We also supply this products to an international market. We also do consultant, and installation of high level security access, alarm and surveillance equipment for medium to large size businesses.

The design should represent a level of trust in our professionalism and expertise. It should visually display our ongoing relationship with the emergency services, but not overtake our commitment to high level security options.

Target Market(s)

Emergency Services and Businesses requiring high level security

Industry/Entity Type

Business

Contact Information for Business Card

*note complete details will be given to the winning designer for revising. The name "Mark Pell will be used to fill in name".

Mark Pell
Managing Director
Corvalt NZ Limited
Phone: +64 027 604 91352
Email: mark.pell@corvalt-example.co.nz

Requirements
Must have
• Card must be in black. Using our logo on the top as supplied. Designers should try having the reverse side as a blurred image of police lights (red and blue) with our logo in greyscale in the centre (this is not particularly a requirement, but feel free to play around with this option).
Nice to have
• A card design that looks good when spot UV printed. A clean compact and graphic design. A grey scale feel on the front (excluding logo, but you can play around with that idea). Rounded smooth text.
Should not have
• Will update this section as designs come through - feel free to submit what you feel would look good.

```html
<!DOCTYPE html>
<html lang="en">
<head>
<meta charset="utf-8">
<title>Corvalt Business Card</title>
<link rel="stylesheet" href="https://fonts.googleapis.com/css2?family=Source+Sans+3:wght@400;600;700&display=swap">
<style>
  :root {
    --backdrop: #3b3b3b;
    --card-black: #060606;
    --card-red: #cf1b21;
    --accent-red: #e0202a;
    --ink-white: #ffffff;
    --ink-soft: #e6e6e6;
    --ink-black: #0a0a0a;
  }
  * { box-sizing: border-box; margin: 0; padding: 0; }
  html, body {
    width: 1105px;
    height: 1200px;
    overflow: hidden;
    background: var(--backdrop);
    font-family: "Source Sans 3", "Segoe UI", sans-serif;
  }
  .canvas { position: relative; width: 1105px; height: 1200px; }
  .card {
    position: absolute;
    left: 196px;
    width: 720px;
    height: 412px;
    overflow: hidden;
  }
  .card--front { top: 146px; background: var(--card-black); }
  .card--back  { top: 602px; background: var(--card-red); }

  .wordmark {
    position: absolute;
    font-weight: 700;
    font-size: 70px;
    line-height: 1;
    letter-spacing: 2px;
    text-transform: uppercase;
  }
  .card--front .wordmark { left: 52px; top: 62px; color: var(--ink-white); }

  .company {
    position: absolute;
    left: 55px;
    top: 268px;
    font-size: 20px;
    color: var(--ink-soft);
  }
  .contact-list {
    position: absolute;
    left: 55px;
    top: 303px;
    list-style: none;
    font-size: 19px;
    color: var(--ink-soft);
  }
  .contact-list li {
    display: flex;
    align-items: center;
    gap: 9px;
    height: 28px;
  }
  .contact-list svg { width: 17px; height: 17px; fill: var(--accent-red); flex: none; }

  .holder {
    position: absolute;
    right: 53px;
    top: 288px;
    text-align: right;
  }
  .holder-name {
    font-size: 25px;
    font-weight: 600;
    color: var(--accent-red);
    text-transform: uppercase;
    line-height: 1.1;
  }
  .holder-role {
    font-size: 20px;
    color: var(--ink-soft);
    line-height: 1.3;
  }

  .back-lockup {
    position: absolute;
    left: 181px;
    top: 190px;
  }
  .card--back .wordmark {
    position: static;
    display: block;
    color: var(--ink-black);
    font-size: 72px;
  }
  .tagline {
    display: block;
    margin-top: -8px;
    font-size: 13px;
    letter-spacing: 6.5px;
    color: var(--ink-black);
    text-transform: uppercase;
  }
</style>
</head>
<body>
<main class="canvas">
  <section class="card card--front" aria-label="Card front">
    <div class="wordmark">Corvalt</div>
    <p class="company">Corvalt NZ Limited</p>
    <ul class="contact-list">
      <li>
        <svg viewBox="0 0 24 24" aria-hidden="true"><path d="M6.6 10.8a15.1 15.1 0 0 0 6.6 6.6l2.2-2.2a1 1 0 0 1 1-.25 11.4 11.4 0 0 0 3.6.57 1 1 0 0 1 1 1V20a1 1 0 0 1-1 1A17 17 0 0 1 3 4a1 1 0 0 1 1-1h3.5a1 1 0 0 1 1 1c0 1.25.2 2.450.57 3.57a1 1 0 0 1-.25 1z"/></svg>
        <span>+64 027 604 91352</span>
      </li>
      <li>
        <svg viewBox="0 0 24 24" aria-hidden="true"><path d="M2 5h20v14H2z M2 5l10 8 10-8" stroke="#060606" stroke-width="1.6"/></svg>
        <span>mark.pell@corvalt-example.co.nz</span>
      </li>
    </ul>
    <div class="holder">
      <p class="holder-name">Mark Pell</p>
      <p class="holder-role">Managing Director</p>
    </div>
  </section>

  <section class="card card--back" aria-label="Card back">
    <div class="back-lockup">
      <span class="wordmark">Corvalt</span>
      <span class="tagline">Ready on arrival</span>
    </div>
  </section>
</main>
</body>
</html>
```